KT Fenwick's Brochure - Brevanta Solutions

Hello,
We have an example of very simple brochure (attached below). We would like you to make it better. More sophisticated. More professional looking. All of the info in the document needs to go in the brochure.
Please let me know if you can execute. I will be happy to send over photos, logos etc, once I know.

```html
<!DOCTYPE html>
<html lang="en">
<head>
<meta charset="utf-8">
<title>KT Fenwick's Brochure – Brevanta Solutions</title>
<link href="https://fonts.googleapis.com/css2?family=Archivo+Black&family=Poppins:wght@400;600;700&display=swap" rel="stylesheet">
<style>
:root{
  --backdrop:#93b0de;
  --navy:#26358a;
  --ink:#111111;
  --body:#222222;
  --grey:#a9a9a9;
  --paper:#ffffff;
}
*{box-sizing:border-box;margin:0;padding:0}
html,body{width:1200px;height:1006px;overflow:hidden;background:var(--backdrop)}
body{position:relative;font-family:"Poppins",sans-serif;color:var(--body)}
.page{position:absolute;width:278px;height:392px;background:var(--paper);overflow:hidden}
.p1{left:138px;top:90px}.p2{left:452px;top:90px}.p3{left:777px;top:90px}
.p4{left:138px;top:524px}.p5{left:452px;top:524px}.p6{left:777px;top:524px}
.photo{position:absolute}
.photo-left{left:0;top:0;width:143px;height:154px}
.photo-right{left:149px;top:0;width:129px;height:183px}
.title{position:absolute;left:18px;top:164px;font-family:"Archivo Black",sans-serif;font-size:21.5px;line-height:23.5px;color:var(--ink);letter-spacing:0;white-space:nowrap}
.title .accent{color:var(--navy)}
.intro{position:absolute;left:18px;right:16px;font-size:7.3px;line-height:11px}
.cols{position:absolute;left:18px;right:10px;display:grid;grid-template-columns:1fr 1fr;column-gap:8px;row-gap:6px;font-size:7.3px;line-height:11px}
.cols li{list-style:none;position:relative;padding-left:7px}
.cols li::before{content:"";position:absolute;left:0;top:4.5px;width:2.4px;height:2.4px;border-radius:50%;background:var(--ink)}
.band{position:absolute;background:var(--navy);color:#fff;font-family:"Archivo Black",sans-serif;display:flex;align-items:center;white-space:nowrap}
.footer{position:absolute;left:0;top:363px;width:278px;height:20px}
.phone{position:absolute;top:0;height:18px;font-size:6.3px;font-weight:700;color:#fff;display:flex;align-items:center;letter-spacing:.2px}
.phone-main{left:0;width:80px;background:var(--navy);padding-left:16px;gap:5px}
.phone-alt{left:82px;width:56px;background:var(--grey);justify-content:center}
.web{position:absolute;left:160px;top:5px;font-size:5.2px}
.brand{position:absolute;right:13px;top:-1px;font-size:8px;font-weight:700;color:var(--navy);letter-spacing:.3px;line-height:20px}
.glass{background:linear-gradient(160deg,#8fb4de 0%,#4f79b4 45%,#2d4a7d 100%)}
.sky{background:linear-gradient(180deg,#a9c6ea 0%,#6f93c4 55%,#4a5e7d 100%)}
.site{background:linear-gradient(180deg,#7b99c2 0%,#5a6f92 60%,#6e7c6a 100%)}
.tower{background:linear-gradient(180deg,#a8c2de 0%,#c9b9a6 60%,#8a5a4a 100%)}
.factory{background:linear-gradient(180deg,#3a4450 0%,#8a939d 50%,#4a5563 100%)}
.office{background:linear-gradient(160deg,#e8ecf2 0%,#9fb1cf 45%,#24408c 100%)}
</style>
</head>
<body>

<section class="page p1">
  <div class="photo photo-left site" role="img" aria-label="Installers setting a glass panel on a high-rise floor"></div>
  <div class="photo photo-right glass" role="img" aria-label="Glass tower rising above a historic street"></div>
  <h1 class="title"><span class="accent">BREVANTA</span><br>SOLUTIONS</h1>
  <ul class="cols" style="top:220px;right:110px;row-gap:4px;font-weight:600">
    <li>Curtain Wall</li><li>Ribbon Window</li><li>Window Wall</li><li>Storefront</li>
  </ul>
  <p class="intro" style="top:256px">Brevanta products can be installed in one third of the time with one third of the installers versus traditional stick products.</p>
  <ul class="cols" style="top:290px;left:15px;row-gap:10px">
    <li>Enclose a building faster allowing other trades to start earlier</li>
    <li>Manufacturing done in a controlled environment</li>
    <li>Standard work and quality control inspections</li>
    <li>Less installers required</li>
  </ul>
  <footer class="footer">
    <div class="phone phone-main"><svg width="7" height="7" viewBox="0 0 24 24"><path fill="#fff" d="M6.6 10.8a15 15 0 0 0 6.6 6.6l2.2-2.2a1 1 0 0 1 1-.25 11.4 11.4 0 0 0 3.6.57 1 1 0 0 1 1 1V20a1 1 0 0 1-1 1A17 17 0 0 1 3 4a1 1 0 0 1 1-1h3.5a1 1 0 0 1 1 1c0 1.25.2 2.45.57 3.57a1 1 0 0 1-.25 1z"/></svg>555-014-0933</div>
    <div class="phone phone-alt">555-014-0640</div>
    <span class="web">www.ktfenwickinc.com</span>
    <span class="brand">FENWICK</span>
  </footer>
</section>

<section class="page p2">
  <div class="photo photo-left sky" role="img" aria-label="Glass office building under a bright sky"></div>
  <div class="photo photo-right glass" role="img" aria-label="Tall curtain wall office tower"></div>
  <h1 class="title"><span class="accent">BREVANTA</span><br>CURTAIN WALL</h1>
  <p class="intro" style="top:217px">Designed by installers for installers with quality and efficient installation. Complete up to 40 panels a day with one installation team.</p>
  <ul class="cols" style="top:262px;row-gap:10px;grid-template-columns:1.15fr 1fr">
    <li>Industry leading 2 1/2" overall adjustment for out of tolerance structures</li>
    <li>Alignment pins allow for 1/4" forgiveness to engage units</li>
    <li>Trim clips and anchors are attached</li>
    <li>Shipped on metal racks or wood crates</li>
  </ul>
  <footer class="footer">
    <div class="phone phone-main"><svg width="7" height="7" viewBox="0 0 24 24"><path fill="#fff" d="M6.6 10.8a15 15 0 0 0 6.6 6.6l2.2-2.2a1 1 0 0 1 1-.25 11.4 11.4 0 0 0 3.6.57 1 1 0 0 1 1 1V20a1 1 0 0 1-1 1A17 17 0 0 1 3 4a1 1 0 0 1 1-1h3.5a1 1 0 0 1 1 1c0 1.25.2 2.45.57 3.57a1 1 0 0 1-.25 1z"/></svg>555-014-0933</div>
    <div class="phone phone-alt">555-014-0640</div>
    <span class="web">www.ktfenwickinc.com</span>
    <span class="brand">FENWICK</span>
  </footer>
</section>

<section class="page p3">
  <div class="photo photo-left sky" role="img" aria-label="Low office building with ribbon windows"></div>
  <div class="photo photo-right glass" role="img" aria-label="Office block with ribbon glazing in winter"></div>
  <h1 class="title"><span class="accent">BREVANTA</span><br>RIBBON WALL<br>STOREFRONT</h1>
  <p class="intro" style="top:240px">Designed for quality and fast installation. This 2" by 4 1/2" system offers the following benefits:</p>
  <ul class="cols" style="top:267px;row-gap:2px">
    <li>Installed from the interior or exterior</li>
    <li>performance due to thermal strut</li>
    <li>Two color option (interior/exterior)</li>
    <li>Shipped on metal racks or wood crates</li>
    <li>Larger panes of glass to improve views</li>
    <li>12 psi water rating</li>
    <li>Higher thermal</li>
  </ul>
  <footer class="footer">
    <div class="phone phone-main"><svg width="7" height="7" viewBox="0 0 24 24"><path fill="#fff" d="M6.6 10.8a15 15 0 0 0 6.6 6.6l2.2-2.2a1 1 0 0 1 1-.25 11.4 11.4 0 0 0 3.6.57 1 1 0 0 1 1 1V20a1 1 0 0 1-1 1A17 17 0 0 1 3 4a1 1 0 0 1 1-1h3.5a1 1 0 0 1 1 1c0 1.25.2 2.45.57 3.57a1 1 0 0 1-.25 1z"/></svg>555-014-0933</div>
    <div class="phone phone-alt">555-014-0640</div>
    <span class="web">www.ktfenwickinc.com</span>
    <span class="brand">FENWICK</span>
  </footer>
</section>

<section class="page p4">
  <div class="photo photo-left sky" role="img" aria-label="Residential high-rise with punched windows"></div>
  <div class="photo photo-right tower" role="img" aria-label="Brick and glass apartment tower"></div>
  <h1 class="title"><span class="accent">SHIPPED</span><br>ON METAL RACKS<br>OR WOOD CRATES</h1>
  <p class="intro" style="top:243px">Designed by installers for an efficient installation with large vision areas. This 6" deep window system offers the following benefits:</p>
  <ul class="cols" style="top:268px;row-gap:2px">
    <li>Punched openings or window wall runs</li>
    <li>Trim clips are attached</li>
    <li>Shipped on metal racks or wood crates</li>
    <li>Metal slab covers</li>
    <li>Installed from the interior using a receptor system.</li>
  </ul>
  <footer class="footer">
    <div class="phone phone-main"><svg width="7" height="7" viewBox="0 0 24 24"><path fill="#fff" d="M6.6 10.8a15 15 0 0 0 6.6 6.6l2.2-2.2a1 1 0 0 1 1-.25 11.4 11.4 0 0 0 3.6.57 1 1 0 0 1 1 1V20a1 1 0 0 1-1 1A17 17 0 0 1 3 4a1 1 0 0 1 1-1h3.5a1 1 0 0 1 1 1c0 1.25.2 2.45.57 3.57a1 1 0 0 1-.25 1z"/></svg>555-014-0933</div>
    <div class="phone phone-alt">555-014-0640</div>
    <span class="web">www.ktfenwickinc.com</span>
    <span class="brand">FENWICK</span>
  </footer>
</section>

<section class="page p5">
  <div class="photo photo-left factory" role="img" aria-label="Assembled glass units racked in the factory"></div>
  <div class="photo photo-right factory" role="img" aria-label="Factory floor with framed panels"></div>
  <h1 class="title"><span class="accent">QUALITY</span><br>CONTROL</h1>
  <div class="band" style="left:0;top:216px;width:232px;height:32px;padding-left:18px;font-size:13px">100% FACTORY ASSEMBLED</div>
  <ul class="cols" style="top:264px;row-gap:2px;grid-template-columns:1fr 1.05fr">
    <li>Temperature Controlled Clean Environment</li>
    <li>Lean Standard Work Training and Certification</li>
    <li>Sealant Manufacture Certification</li>
    <li>Rigorous Quality Inspections</li>
    <li>5% of Completed Units Tested for Air &amp; Water</li>
  </ul>
  <footer class="footer">
    <div class="phone phone-main"><svg width="7" height="7" viewBox="0 0 24 24"><path fill="#fff" d="M6.6 10.8a15 15 0 0 0 6.6 6.6l2.2-2.2a1 1 0 0 1 1-.25 11.4 11.4 0 0 0 3.6.57 1 1 0 0 1 1 1V20a1 1 0 0 1-1 1A17 17 0 0 1 3 4a1 1 0 0 1 1-1h3.5a1 1 0 0 1 1 1c0 1.25.2 2.45.57 3.57a1 1 0 0 1-.25 1z"/></svg>555-014-0933</div>
    <div class="phone phone-alt">555-014-0640</div>
    <span class="web">www.ktfenwickinc.com</span>
    <span class="brand">FENWICK</span>
  </footer>
</section>

<section class="page p6">
  <div class="photo photo-left office" role="img" aria-label="Team planning at a whiteboard in a meeting room"></div>
  <div class="photo photo-right office" role="img" aria-label="Design team working on laptops around a table"></div>
  <h1 class="title" style="top:158px"><span class="accent">DESIGN</span><br>ASSIST</h1>
  <p class="intro" style="top:208px">Through our Charrette Process, we work together with the entire team to identify the Owner's needs, the Architect's design intent, and the Contractor's schedule and budget.</p>
  <div class="band" style="left:0;top:243px;width:143px;height:32px;padding-left:17px;font-size:7.6px">RESOURCES WE PROVIDE :</div>
  <div class="band" style="left:149px;top:243px;width:129px;height:32px;padding-left:21px;font-size:7.6px">TOOLS WE USE:</div>
  <ul class="cols" style="top:282px;left:20px;column-gap:0;row-gap:0;grid-template-columns:150px 1fr;grid-auto-flow:column;grid-template-rows:repeat(7,auto)">
    <li>Curtain Wall Designer</li><li>Architect</li><li>Structural Engineer</li><li>Estimator</li><li>Project Manager</li><li style="visibility:hidden">-</li><li style="visibility:hidden">-</li>
    <li>Vextra for BIM Models</li><li>Decision Matrix</li><li>Mind Map</li><li>Elevation Map</li><li>Document Tracking</li><li>Budget Updates</li><li>Product Samples</li>
  </ul>
  <footer class="footer">
    <div class="phone phone-main"><svg width="7" height="7" viewBox="0 0 24 24"><path fill="#fff" d="M6.6 10.8a15 15 0 0 0 6.6 6.6l2.2-2.2a1 1 0 0 1 1-.25 11.4 11.4 0 0 0 3.6.57 1 1 0 0 1 1 1V20a1 1 0 0 1-1 1A17 17 0 0 1 3 4a1 1 0 0 1 1-1h3.5a1 1 0 0 1 1 1c0 1.25.2 2.45.57 3.57a1 1 0 0 1-.25 1z"/></svg>555-014-0933</div>
    <div class="phone phone-alt">555-014-0640</div>
    <span class="web">www.ktfenwickinc.com</span>
    <span class="brand">FENWICK</span>
  </footer>
</section>

</body>
</html>
```